Menu Design Project for new restauranct concept

Design menu for new restaurant concept called Juniper's Burgers & Dogs. Logo is attached.

Industry/Entity Type

Restaurant

Requirements
Must have
• Menu items and pricing:

Burgers
Snack Burger $3.49
Snack Cheeseburger $3.99
Juniper's signature Burger $4.99
Juniper's signature Cheeseburger $5.49
Burger toppings: bacon, lettuce, tomato, onion, pickle, grilled onions, grilled mushrooms, grilled green peppers, jalapeƱo peppers.

Dogs
Hot Dog $2.99
Bacon Cheese Hot Dog $3.99
Slaw Dog $3.99
Kraut Dog $3.49
Chili Dog $3.99 with or with out cheese
Hot dogs are 100% beef

Other
Grilled Chicken Sandwich $5.99
Grilled Chicken Sandwich with cheese $6.49
(Same toppings as burgers)

French Fries $1.99

Loaded Potatos
The Plain Tater: $4.99 choose from: butter, sour cream, cheese, chives
The Garden Tater: $5.99 choose from: the Basic plus, broccoli & cheese, grilled mushrooms, onions, & peppers
The Rancher Tater: $6.99 choose from the Basic/Veggie plus: grilled chicken, chili, Philly cheesesteak, pulled pork.

Drinks
32oz. Drink $1.88
20oz. Drink $1.69

attached logo.
Nice to have
• love to incorporate the woodgrain backgound. It makes the logo look most like a cattle brand, which we like.

```html
<!DOCTYPE html>
<html lang="en">
<head>
<meta charset="utf-8">
<title>Juniper's Burgers &amp; Dogs — Menu</title>
<link href="https://fonts.googleapis.com/css2?family=EB+Garamond:wght@400;700&display=swap" rel="stylesheet">
<style>
  :root {
    --wood-light: #978c80;
    --wood-mid: #7d7369;
    --wood-dark: #635a52;
    --panel: rgba(14, 11, 9, 0.92);
    --panel-edge: rgba(0, 0, 0, 0.5);
    --heading: #bba58a;
    --item: #ab9c89;
    --brand: #1c1916;
  }
  * { margin: 0; padding: 0; box-sizing: border-box; }
  html, body { width: 1000px; height: 1200px; overflow: hidden; }
  body { font-family: "EB Garamond", Georgia, serif; color: var(--item); }
  .menu { position: relative; width: 1000px; height: 1200px; }
  .wood-backdrop {
    position: absolute; inset: 0;
    background:
      linear-gradient(90deg, var(--wood-mid) 0%, var(--wood-light) 18%, var(--wood-dark) 34%, var(--wood-light) 52%, var(--wood-mid) 70%, var(--wood-light) 86%, var(--wood-dark) 100%);
  }
  .brand {
    position: absolute; left: 0; top: 110px; width: 1000px;
    text-align: center; color: var(--brand); font-weight: 700;
  }
  .brand-name { font-size: 92px; line-height: 1; }
  .brand-tag { font-size: 44px; line-height: 1; margin-top: 40px; letter-spacing: 1px; }
  .panel {
    position: absolute; background: var(--panel);
    border: 1px solid var(--panel-edge); border-radius: 3px;
  }
  .panel-title {
    color: var(--heading); font-weight: 400; text-align: center;
    font-size: 35px; line-height: 1;
  }
  .item-row {
    display: flex; justify-content: space-between;
    font-weight: 700; font-size: 17.5px; line-height: 29px;
  }
  .item-note { font-size: 15px; }
  .burgers { left: 48px; top: 383px; width: 902px; height: 303px; }
  .burgers .panel-title { margin-top: 14px; }
  .burgers .columns { display: flex; gap: 42px; padding: 0 14px 0 14px; margin-top: 16px; }
  .burgers .column { flex: 1; }
  .burgers .column:first-child { flex: 0 0 404px; }
  .fries { text-align: center; font-weight: 700; font-size: 17.5px; margin-top: 14px; }
  .toppings { text-align: center; font-weight: 700; font-size: 17.5px; line-height: 23px; margin: 12px 30px 0; }
  .dogs { left: 33px; top: 713px; width: 450px; height: 303px; }
  .dogs .panel-title { margin-top: 12px; }
  .dogs .list { padding: 0 20px 0 10px; margin-top: 18px; }
  .dogs .item-row { line-height: 26px; }
  .beef-note { text-align: center; font-weight: 700; font-size: 17.5px; margin-top: 14px; }
  .potatoes { left: 514px; top: 713px; width: 457px; height: 303px; }
  .potatoes .panel-title { margin-top: 12px; }
  .potatoes .list { padding: 0 30px 0 12px; margin-top: 18px; }
  .tater { margin-bottom: 18px; font-weight: 700; font-size: 17.5px; line-height: 21px; }
  .tater .item-row { line-height: 21px; }
  .tater-options { margin-right: -22px; }
  .drinks { left: 361px; top: 1046px; width: 277px; height: 114px; }
  .drinks .panel-title { font-size: 32px; margin-top: 10px; }
  .drinks .list { padding: 0 18px 0 12px; margin-top: 8px; }
</style>
</head>
<body>
<main class="menu">
  <div class="wood-backdrop" role="img" aria-label="Weathered grey woodgrain plank texture"></div>

  <header class="brand">
    <div class="brand-name">Juniper's</div>
    <div class="brand-tag">BURGERS &amp; DOGS</div>
  </header>

  <section class="panel burgers">
    <h2 class="panel-title">Burgers &amp; Sandwiches</h2>
    <div class="columns">
      <div class="column">
        <div class="item-row"><span>Snack Burger</span><span>$3.49</span></div>
        <div class="item-row"><span>Snack Cheeseburger</span><span>$3.99</span></div>
        <div class="item-row"><span>Grilled Chicken Sandwich</span><span>$5.99</span></div>
      </div>
      <div class="column">
        <div class="item-row"><span>Juniper's signature Burger</span><span>$4.99</span></div>
        <div class="item-row"><span>Juniper's signature Cheeseburger</span><span>$5.49</span></div>
        <div class="item-row"><span>Grilled Chicken Sandwich <span class="item-note">with cheese</span></span><span>$6.49</span></div>
      </div>
    </div>
    <p class="fries">French Fries $ 1.99</p>
    <p class="toppings">Burger/Sandwich toppings: bacon, lettuce, tomato, onion, pickle, grilled onions, grilled mushrooms, grilled green peppers, jalapeño peppers.</p>
  </section>

  <section class="panel dogs">
    <h2 class="panel-title">Dogs</h2>
    <div class="list">
      <div class="item-row"><span>Hot Dog</span><span>$2.99</span></div>
      <div class="item-row"><span>Bacon Cheese Hot Dog</span><span>$3.99</span></div>
      <div class="item-row"><span>Slaw Dog</span><span>$3.99</span></div>
      <div class="item-row"><span>Kraut Dog</span><span>$3.49</span></div>
      <div class="item-row"><span>Chili Dog with or with out cheese</span><span>$3.99</span></div>
    </div>
    <p class="beef-note">Hot dogs are 100% beef</p>
  </section>

  <section class="panel potatoes">
    <h2 class="panel-title">Loaded Potatoes</h2>
    <div class="list">
      <div class="tater">
        <div class="item-row"><span>The Plain Tater</span><span>$4.99</span></div>
        <p class="tater-options">choose from: butter, sour cream, cheese, chives</p>
      </div>
      <div class="tater">
        <div class="item-row"><span>The Garden Tater</span><span>$5.99</span></div>
        <p class="tater-options">choose from: the Basic plus, broccoli &amp; cheese, grilled mushrooms, onions, &amp; peppers</p>
      </div>
      <div class="tater">
        <div class="item-row"><span>The Rancher Tater:</span><span>$6.99</span></div>
        <p class="tater-options">choose from the Basic/Veggie plus: grilled chicken, chili, Philly cheesesteak, pulled pork.</p>
      </div>
    </div>
  </section>

  <section class="panel drinks">
    <h2 class="panel-title">Drinks</h2>
    <div class="list">
      <div class="item-row"><span>32 oz. Drink</span><span>$1.88</span></div>
      <div class="item-row"><span>20 oz. Drink</span><span>$1.69</span></div>
    </div>
  </section>
</main>
</body>
</html>
```